Brantley Water Taxi and Transport

Need to redesign our business cards to relay that we do freight logistics and water taxi service. We also work with gov. agencies doing environmental clean up, oil spill response, remote site construction and work with many of the air taxi and helicopter services on Kodiak Island. Out website is www.brantleywatertaxi-example.com to get a better idea of what we do.

Contact Information for Business Card

I have a previous business card but it just has the logo on the front, and a sunset picture on the back with the contact info. It does not relay what we do and what we can help with. I like a simple straight forward design over a busy one.

Colors
3176b5
0455a3
cfdfed

Requirements
Must have
• logo, email, website, phone number

```html
<!DOCTYPE html>
<html lang="en">
<head>
<meta charset="utf-8">
<title>Brantley Water Taxi and Transport – Business Cards</title>
<link href="https://fonts.googleapis.com/css2?family=Jost:wght@400;500;600&display=swap" rel="stylesheet">
<style>
  :root {
    --backdrop: #bfe6dd;
    --card: #fbfbfa;
    --navy: #0e4a94;
    --sky: #3fb3e3;
    --ink: #1f2a33;
    --icon: #0e4a94;
  }
  * { box-sizing: border-box; margin: 0; padding: 0; }
  html, body {
    width: 1200px; height: 800px; overflow: hidden;
    background: var(--backdrop);
    font-family: "Jost", "Futura", sans-serif;
  }
  .card {
    position: absolute;
    top: 278px;
    width: 419px; height: 240px;
    background: var(--card);
    box-shadow: 0 6px 14px rgba(40, 90, 80, 0.25);
  }
  .card--front { left: 142px; }
  .card--back { left: 638px; }

  /* Front */
  .front-mark {
    position: absolute;
    left: 176px; top: 40px;
    width: 66px; height: 66px;
    border-radius: 50%;
    background: var(--sky);
  }
  .front-name {
    position: absolute;
    left: 0; right: 0; top: 126px;
    text-align: center;
    color: var(--navy);
    font-weight: 600;
    font-size: 48px;
    line-height: 1;
    letter-spacing: 0.5px;
    white-space: nowrap;
  }
  .front-tagline {
    position: absolute;
    left: 0; right: 0; top: 186px;
    text-align: center;
    color: var(--ink);
    font-weight: 400;
    font-size: 20px;
    line-height: 1;
    letter-spacing: 0.4px;
    white-space: nowrap;
  }

  /* Back */
  .back-name {
    position: absolute;
    left: 44px; top: 46px;
    color: var(--navy);
    font-weight: 600;
    font-size: 38px;
    line-height: 1;
    letter-spacing: 0.5px;
    white-space: nowrap;
  }
  .back-tagline {
    position: absolute;
    left: 45px; top: 86px;
    color: var(--ink);
    font-weight: 400;
    font-size: 16px;
    line-height: 1;
    letter-spacing: 0.3px;
    white-space: nowrap;
  }
  .contact-list {
    position: absolute;
    left: 132px; top: 136px;
    list-style: none;
  }
  .contact-item {
    display: flex;
    align-items: center;
    height: 20px;
    margin-bottom: 1px;
    color: var(--ink);
    font-size: 14px;
    line-height: 1;
    font-weight: 400;
    white-space: nowrap;
  }
  .contact-icon {
    width: 13px; height: 13px;
    margin-right: 14px;
    flex: none;
  }
</style>
</head>
<body>

  <section class="card card--front">
    <div class="front-mark"></div>
    <div class="front-name">BRANTLEY</div>
    <div class="front-tagline">Water Taxi &amp; Transport</div>
  </section>

  <section class="card card--back">
    <div class="back-name">BRANTLEY</div>
    <div class="back-tagline">Water Taxi &amp; Transport</div>
    <ul class="contact-list">
      <li class="contact-item">
        <svg class="contact-icon" viewBox="0 0 14 14" aria-hidden="true">
          <circle cx="7" cy="7" r="7" fill="var(--icon)"/>
          <path d="M4.6 3.6c.4-.3.8-.2 1 .2l.6 1.2c.2.4 0 .7-.3.9l-.4.3c.3.9 1 1.6 1.9 2l.3-.4c.2-.3.6-.4.9-.2l1.2.6c.4.2.5.6.2 1l-.5.6c-.4.4-1 .5-1.6.2-1.7-.8-3-2.1-3.7-3.8-.2-.6-.1-1.2.4-1.6z" fill="#fff"/>
        </svg>
        555 010 3400
      </li>
      <li class="contact-item">
        <svg class="contact-icon" viewBox="0 0 14 14" aria-hidden="true">
          <rect x="0" y="2.5" width="14" height="9" fill="var(--icon)"/>
          <path d="M0.5 3l6.5 5 6.5-5M0.5 11l4.5-4M13.5 11l-4.5-4" stroke="#fff" stroke-width="1" fill="none"/>
        </svg>
        brantleywatertaxi@example.com
      </li>
      <li class="contact-item">
        <svg class="contact-icon" viewBox="0 0 14 14" aria-hidden="true">
          <circle cx="7" cy="7" r="7" fill="var(--icon)"/>
          <path d="M0 7h14M7 0c-2.5 2-2.5 12 0 14M7 0c2.5 2 2.5 12 0 14M1.5 3.8h11M1.5 10.2h11" stroke="#fff" stroke-width="0.8" fill="none"/>
        </svg>
        www.brantleywatertaxi-example.com
      </li>
    </ul>
  </section>

</body>
</html>
```